Beyond the Hunt Product Labeling

We need a label design for a new product we are launching. We have developed a cooking bag that will cook your fish or game bird instantly. This is for the everyday fisherman and upland game hunter. This label will be printed on a thin sticker on the front of a Mylar Bag. The Mylar Bag is 9 1/2 x 12 inches. Inside the Mylar Bag is 3 cooking bags.
Target Market(s)
hunters and fishermen
Industry/Entity Type
Cooking
Font styles to use
Sans Serif
Colors
Designer to choose colors to be used in the design.
Requirements
Must have
- It must have "Beyond the Hunt" logo. It should have Scale and Plume. Scale and Plume is the type of seasoning. It must have a small place on the label for net weight. It must also have the wording "Contains: 3 Individual Cooking Bags Inside.
Nice to have
- I really like a topographical map in the background. I have attached several images with products like that. It could also be cool having the background of the bag with a tiger trout's scales. I attached some images of that too. Some other ideas I thought i have is having a picture of the bird and fish on the bag. There is an GIF attached that has a cool looking fish that did that. There is also an image of a Holvak product that did the same thing.

```html
<!DOCTYPE html>
<html lang="en">
<head>
<meta charset="utf-8">
<title>Beyond the Hunt – Cooking Bag Label</title>
<link href="https://fonts.googleapis.com/css2?family=Oswald:wght@600&family=Lato:wght@700&display=swap" rel="stylesheet">
<style>
  :root {
    --silver-light: #f1f1f1;
    --silver-mid: #d9d9d9;
    --silver-dark: #bdbdbd;
    --label-yellow: #e3dc3a;
    --ink: #111111;
  }
  html, body {
    margin: 0;
    padding: 0;
    width: 966px;
    height: 1200px;
    overflow: hidden;
    background: var(--silver-light);
  }
  .bag-face {
    position: relative;
    width: 966px;
    height: 1200px;
    overflow: hidden;
  }
  .topo-background {
    position: absolute;
    inset: 0;
    background: radial-gradient(ellipse at 40% 30%, var(--silver-light) 0%, var(--silver-mid) 55%, var(--silver-dark) 100%);
  }
  .label-shape {
    position: absolute;
    inset: 0;
  }
  .artwork {
    position: absolute;
    border-radius: 8px;
  }
  .artwork--elk-mountains {
    left: 232px; top: 270px; width: 436px; height: 172px;
    background: linear-gradient(135deg, rgba(17,17,17,0.55), rgba(17,17,17,0.2));
  }
  .artwork--bird-fish {
    left: 193px; top: 618px; width: 555px; height: 132px;
    background: linear-gradient(90deg, rgba(17,17,17,0.6), rgba(17,17,17,0.35));
  }
  .brand-name {
    position: absolute;
    right: 166px;
    top: 452px;
    margin: 0;
    font-family: "Oswald", sans-serif;
    font-weight: 600;
    font-size: 80px;
    line-height: 1;
    letter-spacing: -1px;
    color: var(--ink);
    white-space: nowrap;
  }
  .seasoning-name {
    position: absolute;
    right: 168px;
    top: 550px;
    margin: 0;
    font-family: "Oswald", sans-serif;
    font-weight: 600;
    font-size: 34px;
    line-height: 1;
    letter-spacing: 1px;
    color: var(--ink);
    white-space: nowrap;
  }
  .rule {
    position: absolute;
    left: 203px;
    width: 567px;
    height: 2px;
    background: var(--ink);
  }
  .rule--top { top: 757px; }
  .rule--bottom { top: 841px; }
  .contents {
    position: absolute;
    left: 183px;
    width: 607px;
    top: 768px;
    margin: 0;
    text-align: center;
    font-family: "Lato", sans-serif;
    font-weight: 700;
    font-size: 24px;
    line-height: 33px;
    color: var(--ink);
  }
  .net-weight {
    position: absolute;
    left: 283px;
    width: 400px;
    top: 890px;
    margin: 0;
    text-align: center;
    font-family: "Lato", sans-serif;
    font-weight: 700;
    font-size: 23px;
    line-height: 33px;
    color: var(--ink);
  }
</style>
</head>
<body>
  <main class="bag-face">
    <div class="topo-background" role="img" aria-label="Silver background with grey topographic contour map lines"></div>

    <svg class="label-shape" width="966" height="1200" viewBox="0 0 966 1200" aria-hidden="true">
      <polygon points="483,98 838,298 838,830 483,1064 128,830 128,298"
               fill="var(--silver-light)" stroke="var(--ink)" stroke-width="6"/>
      <polygon points="483,120 820,310 820,818 483,1042 146,818 146,310"
               fill="var(--label-yellow)"/>
    </svg>

    <div class="artwork artwork--elk-mountains" role="img" aria-label="Black illustration of a bugling elk head beside mountain peaks"></div>

    <h1 class="brand-name">BEYOND THE HUNT</h1>
    <p class="seasoning-name">SCALE AND PLUME</p>

    <div class="artwork artwork--bird-fish" role="img" aria-label="Black silhouette of a game bird beside a leaping trout illustration"></div>

    <div class="rule rule--top"></div>
    <p class="contents">CONTAINS:<br>3 INDIVIDUAL COOKING BAGS INSIDE</p>
    <div class="rule rule--bottom"></div>

    <p class="net-weight">Net Weight<br>75gm oz</p>
  </main>
</body>
</html>
```